Real Estate Brochure/ door flyer.

I am looking for a brochure that can be put in a plastic door hanger bag and distributed as I walk throughout neighborhoods. It should be mainly directed towards Sellers, but have a nod to Buyers as well since once sold, the person will need to buy.
I was planning on a tri fold brochure, but am open to other styles. I do have a bio, and am on the fence as to whether or not to include it.

Target Market(s)

Owners of residential homes and potential buyers of the same

Industry/Entity Type

Real Estate

Colors

Designer to choose colors to be used in the design.

Requirements
Must have
• The service promises I have made, our logo,
• My contact information, email and cell phone.
• I'm looking for something bright and clean looking.
• There is an equal housing opportunity symbol and Dwellmark symbol that is required by law, I am trying to find artwork for it. As well as "Not intended to solicit represented parties" has to be on the brochure somewhere.
Nice to have
• Photos of homeowner's in a nice home. I like mixed family relationships. Interracial, same sex couples and young couples just starting out.
Should not have
• Any form of deadline or timeline to respond.

```html
<!DOCTYPE html>
<html lang="en">
<head>
<meta charset="utf-8">
<title>Seller Services Brochure</title>
<link rel="stylesheet" href="https://fonts.googleapis.com/css2?family=Source+Sans+3:wght@400;500&display=swap">
<style>
  :root {
    --brand-red: #e8202a;
    --ink-navy: #1f2a7a;
    --title-blue: #34409a;
    --star-yellow: #f4e500;
    --paper: #ffffff;
  }
  * { margin: 0; padding: 0; box-sizing: border-box; }
  html, body { width: 1200px; height: 933px; overflow: hidden; background: var(--paper); }
  body { font-family: "Source Sans 3", "Myriad Pro", Arial, sans-serif; }
  .brochure { position: relative; width: 1200px; height: 933px; overflow: hidden; }
  .red-field { position: absolute; inset: 0; }
  .hero-photo {
    position: absolute; left: 12px; top: 12px; width: 380px; height: 400px;
    border-top-left-radius: 28px;
    background:
      linear-gradient(to bottom, rgba(255,255,255,0) 60%, #ffffff 100%),
      radial-gradient(ellipse at 30% 70%, #f1d3bd 0%, rgba(241,211,189,0) 40%),
      linear-gradient(120deg, #c9d7a2 0%, #a9c27a 35%, #e7e3d3 70%, #cfc3ad 100%);
  }
  .panel-title {
    position: absolute; font-weight: 400; font-size: 26px; line-height: 35px;
    text-align: center;
  }
  .panel-title--seller { left: 22px; top: 424px; width: 368px; color: var(--title-blue); }
  .panel-title--buyer { left: 395px; top: 656px; width: 393px; color: #fff; }
  .promise-list {
    position: absolute; list-style: none; font-size: 21px; line-height: 28.6px;
    text-align: justify; hyphens: manual;
  }
  .promise-list li { margin-bottom: 28.6px; }
  .promise-list--left { left: 27px; top: 568px; width: 358px; color: var(--ink-navy); }
  .promise-list--middle { left: 405px; top: 14px; width: 370px; color: var(--ink-navy); }
  .promise-list--bottom { left: 405px; top: 794px; width: 370px; color: #fff; text-align: left; }
  .promise-list--right { left: 803px; top: 54px; width: 366px; color: #fff; }
  .star { font-size: 22px; margin-right: 6px; }
  .star--red { color: var(--brand-red); }
  .star--yellow { color: var(--star-yellow); }
  .slider-mark { position: absolute; left: 855px; top: 834px; }
</style>
</head>
<body>
<main class="brochure">
  <svg class="red-field" width="1200" height="933" viewBox="0 0 1200 933" aria-hidden="true">
    <path fill="#e8202a" d="M423 632 H753 A35 35 0 0 0 788 597 V40 A28 28 0 0 1 816 12 H1155 A28 28 0 0 1 1183 40 V891 A28 28 0 0 1 1155 919 H415 A20 20 0 0 1 395 899 V660 A28 28 0 0 1 423 632 Z"/>
  </svg>

  <div class="hero-photo" role="img" aria-label="Photo of a hand passing a house key on a ring with a small house keychain, green lawn and home behind"></div>

  <h2 class="panel-title panel-title--seller">My Promise of&nbsp; Services<br>to the Seller as a Professional<br>Real Estate Agent</h2>

  <ul class="promise-list promise-list--left">
    <li><span class="star star--red">✱</span>Professional courteous com&shy;munication. With weekly updates and feedback from Agents and the potential Buyers that have been through your home.</li>
    <li><span class="star star--red">✱</span>No Lockboxes! I do not sub&shy;scribe to an Agent putting a lockbox on your home and disappearing, only to miraculously show up at the closing. I will meet all potential Buyers and walk them through your</li>
  </ul>

  <ul class="promise-list promise-list--middle">
    <li>home, pointing out it’s highlights and enlisting their feedback on your home.</li>
    <li><span class="star star--red">✱</span>I will provide professional advice on how to stage and prepare your home for a showing from the prospective of the Buyer.</li>
    <li><span class="star star--red">✱</span>Open Houses. I make every attempt to perform two open houses every month. Yours could be next!</li>
    <li><span class="star star--red">✱</span>Referral system. Not ready to sell? Maybe you know someone that is considering selling or someone looking to buy a home. Send me their contact information and if it leads to a sale or a purchase, I will give you a gift certificate good for dinner for two at a local restaurant!</li>
  </ul>

  <h2 class="panel-title panel-title--buyer">My Promise of&nbsp; Services<br>to the Seller as a Professional<br>Real Estate Agent</h2>

  <ul class="promise-list promise-list--bottom">
    <li><span class="star star--yellow">✱</span>I will work with to help you find a property that fits your needs as well as your budget.</li>
  </ul>

  <ul class="promise-list promise-list--right">
    <li><span class="star star--yellow">✱</span>I can put you together with a mortgage professional to get you prequalified for a mortgage that fits your budget.</li>
    <li><span class="star star--yellow">✱</span>I will be with you during all inspections to make sure you are comfortable with the property you are purchasing.</li>
    <li><span class="star star--yellow">✱</span>I will communicate and negoti&shy;ate with the Seller or Seller’s agent on your behalf.</li>
    <li><span class="star star--yellow">✱</span>I will work with your mortgage broker and your attorney to keep things on schedule.</li>
    <li><span class="star star--yellow">✱</span>I will communicate with you from the day of the initial showing to the final walk through and closing of your new home, so that you are com&shy;fortable with where you are in the process and know what you can expect next.</li>
  </ul>

  <svg class="slider-mark" width="276" height="20" viewBox="0 0 276 20" aria-hidden="true">
    <line x1="8" y1="10" x2="268" y2="10" stroke="#fff" stroke-width="2"/>
    <circle cx="8" cy="10" r="7" fill="#fff"/>
    <circle cx="268" cy="10" r="7" fill="#fff"/>
  </svg>
</main>
</body>
</html>
```